2026 Halden Voyra medium roof

Van voyra logo wrap, construction company Copper Lane Renovations LLC

Target Market(s)

More customers

Industry/Entity Type

License contractor, remodeling, construction

Colors

Designer to choose colors to be used in the design.

Requirements
Must have
• House logo, jobs I offer, phone number,, license & insured , QVR acquitted business,
Nice to have
• I would like to have the QVR logo in lower right bottom of van

```html
<!DOCTYPE html>
<html lang="en">
<head>
<meta charset="utf-8">
<title>Copper Lane Renovations LLC — Halden Voyra van wrap</title>
<link rel="stylesheet" href="https://fonts.googleapis.com/css2?family=Source+Sans+3:wght@400;600;700&display=swap">
<style>
  :root {
    --page: #f2f2f0;
    --body-grey: #c9ccd1;
    --body-light: #dfe1e4;
    --navy: #1f3f63;
    --slate: #586b80;
    --trim: #1d1f22;
    --wood-light: #c79a6c;
    --wood-dark: #a47650;
    --glass: #2a2d31;
    --gold: #d8b458;
    --cream: #f4ede2;
    --photo-a: #b8b4ae;
    --photo-b: #8d7a66;
    --tire: #222426;
    --rim: #b7bbbf;
  }
  html, body {
    margin: 0;
    padding: 0;
    width: 1200px;
    height: 523px;
    overflow: hidden;
    background: var(--page);
  }
  .wrap-canvas { display: block; width: 1200px; height: 523px; }
  .wrap-canvas text { font-family: "Source Sans 3", "Segoe UI", sans-serif; }
  .services-title { font-size: 21px; font-weight: 700; fill: var(--navy); }
  .service-item { font-size: 9.6px; font-weight: 400; fill: var(--navy); }
  .brand-line1 { font-size: 29px; font-weight: 700; fill: var(--navy); letter-spacing: 0.2px; }
  .brand-line2 { font-size: 23px; font-weight: 700; fill: var(--navy); letter-spacing: 0.4px; }
  .web-address { font-size: 17px; font-weight: 600; fill: #ffffff; letter-spacing: 2.6px; }
  .tagline { font-size: 18.5px; font-weight: 600; fill: var(--navy); letter-spacing: 1.4px; }
  .phone-number { font-size: 23px; font-weight: 700; fill: var(--cream); }
  .license-note { font-size: 9px; fill: var(--navy); }
  .license-note .label { font-weight: 700; }
  .badge-caption { font-size: 9.5px; font-weight: 700; fill: #f3f3f3; letter-spacing: 0.3px; }
</style>
</head>
<body>
<svg class="wrap-canvas" viewBox="0 0 1200 523" xmlns="http://www.w3.org/2000/svg">
  <defs>
    <linearGradient id="wood-tone" x1="0" y1="0" x2="1" y2="1">
      <stop offset="0" stop-color="var(--wood-light)"/>
      <stop offset="1" stop-color="var(--wood-dark)"/>
    </linearGradient>
    <linearGradient id="crew-tone" x1="0" y1="0" x2="1" y2="0">
      <stop offset="0" stop-color="var(--photo-a)" stop-opacity="0"/>
      <stop offset="0.25" stop-color="var(--photo-a)"/>
      <stop offset="1" stop-color="var(--photo-b)"/>
    </linearGradient>
    <clipPath id="van-body">
      <path d="M70 370 L80 300 Q100 265 150 250 L320 80 Q380 58 470 56 L1090 54 Q1125 56 1130 90 L1140 360 L1140 420 L70 420 Z"/>
    </clipPath>
  </defs>

  <g class="van-shell">
    <path d="M70 370 L80 300 Q100 265 150 250 L320 80 Q380 58 470 56 L1090 54 Q1125 56 1130 90 L1140 360 L1140 420 L70 420 Z" fill="var(--body-grey)"/>
    <g clip-path="url(#van-body)">
      <rect x="0" y="0" width="1200" height="523" fill="var(--body-light)" opacity="0.5"/>
      <path class="wood-panel" role="img" aria-label="Wood deck plank texture" d="M60 250 L360 120 L900 175 L1140 230 L1140 345 L880 345 L470 275 L300 370 L60 372 Z" fill="url(#wood-tone)"/>
      <rect class="crew-photo" role="img" aria-label="Photo of a drywall worker and a siding installer at work" x="690" y="95" width="450" height="265" fill="url(#crew-tone)"/>
      <path d="M300 372 L470 278 L880 348 L1140 350 L1140 420 L300 420 Z" fill="var(--body-grey)"/>
    </g>
    <path d="M190 285 L262 155 Q272 132 300 130 L430 130 Q440 132 438 150 L430 262 Q428 276 410 280 L240 285 Z" fill="var(--glass)"/>
    <path d="M82 322 L92 290 L150 272 L140 318 Z" fill="#d9dce0" opacity="0.8"/>
    <path d="M55 370 L1145 360 L1145 420 L300 430 L55 420 Z" fill="var(--trim)"/>
    <rect x="300" y="412" width="560" height="22" fill="var(--body-grey)"/>
    <rect x="1108" y="245" width="24" height="120" rx="6" fill="#b3221f"/>
    <g class="wheel">
      <circle cx="212" cy="440" r="66" fill="var(--trim)"/>
      <circle cx="212" cy="440" r="56" fill="var(--tire)"/>
      <circle cx="212" cy="440" r="38" fill="var(--rim)"/>
      <circle cx="212" cy="440" r="12" fill="#8c9094"/>
    </g>
    <g class="wheel">
      <circle cx="934" cy="440" r="66" fill="var(--trim)"/>
      <circle cx="934" cy="440" r="56" fill="var(--tire)"/>
      <circle cx="934" cy="440" r="38" fill="var(--rim)"/>
      <circle cx="934" cy="440" r="12" fill="#8c9094"/>
    </g>
  </g>

  <g class="services">
    <text class="services-title" x="466" y="93">Services</text>
    <text class="service-item" x="627" y="79">• Kitchens &amp; Bathrooms</text>
    <text class="service-item" x="627" y="93">• Drywall &amp; Painting</text>
    <text class="service-item" x="740" y="79">• Plumbing &amp; Electrical</text>
    <text class="service-item" x="740" y="93">• Doors &amp; Windows</text>
    <text class="service-item" x="845" y="79">• Flooring</text>
    <text class="service-item" x="845" y="93">• Interior &amp; Exterior</text>
    <text class="service-item" x="934" y="79">• Roofing</text>
    <text class="service-item" x="934" y="93">• Siding</text>
    <text class="service-item" x="990" y="79">• Decks</text>
    <text class="service-item" x="990" y="93">• Fences</text>
  </g>

  <g class="brand">
    <rect x="556" y="150" width="76" height="76" fill="var(--navy)"/>
    <text class="brand-line1" x="594" y="267" text-anchor="middle">COPPER LANE</text>
    <text class="brand-line2" x="594" y="291" text-anchor="middle">RENOVATIONS LLC</text>
  </g>

  <g class="web-ribbon">
    <path d="M377 313 L405 299 L785 299 L810 313 L785 328 L405 328 Z" fill="var(--navy)"/>
    <text class="web-address" x="594" y="320" text-anchor="middle">COPPERLANERENOVATIONS.COM</text>
  </g>

  <text class="tagline" x="594" y="352" text-anchor="middle">LICENSED · INSURED · TRUSTED</text>

  <g class="phone">
    <circle cx="167" cy="316" r="13" fill="none" stroke="var(--gold)" stroke-width="2"/>
    <path d="M161 309 q2 -2 4 0 l2 3 q1 2 -1 3 q1 3 4 5 q1 -2 3 -1 l3 2 q2 2 0 4 q-3 3 -8 0 q-6 -4 -8 -9 q-2 -4 1 -7 Z" fill="var(--gold)"/>
    <text class="phone-number" x="186" y="324">(555) 014-2290</text>
  </g>

  <g class="accreditation">
    <rect x="1034" y="239" width="56" height="74" rx="4" fill="none" stroke="#f1f1f1" stroke-width="1.5"/>
    <text class="badge-caption" x="1062" y="332" text-anchor="middle">PROUD TO BE</text>
    <text class="badge-caption" x="1062" y="344" text-anchor="middle">ACCREDITED</text>
  </g>

  <text class="license-note" x="594" y="428" text-anchor="middle"><tspan class="label">License #:</tspan> 241900386</text>
</svg>
</body>
</html>
```